Super Greens Label for Supplement Bottle

We want to design a front label for a health supplement bottle. The product is called Leafy Blendbite Chews™. This will be a new product so there is no current website for the product. The focus is on supergreens that taste great and deliver support for energy, digestion, and immune defense.
We want it to be modern, vibrant and appealing.
Bottle size: standard size supplement CLEAR bottle size, with white child resistant cap and the label panel dimensions are 3” x 7”. The label should be primarily white and green, with a touch of red; (see color palettes)/it can also ONLY be white and green. See samples attached.
We are only focused on the front of the bottle design, not on the back, but leave space for the supplement panel and other text on the back.
So the text for the front of the bottle is:
RT Dalloway's
Leafy Blendbite Chews™
Super Greens Blend for:
Energy, Digestion, and Immune Support*
60 Gummies | Dietary Supplement
Raspberry Flavor Gummies
Off to side of the label:
Non-GMO
Vegan Friendly
Plant-Based
Gelatin Free
Colors
Designer to choose colors to be used in the design.
Look and feel
Each slider illustrates characteristics of the customer's brand and the style your logo design should communicate.

```html
<!DOCTYPE html>
<html lang="en">
<head>
<meta charset="UTF-8">
<title>RT Dalloway's Leafy Blendbite Chews – Front Label</title>
<link href="https://fonts.googleapis.com/css2?family=Montserrat:wght@300;500;600;800&family=Oswald:wght@300&display=swap" rel="stylesheet">
<style>
  :root {
    --bg: #eeeff0;
    --paper: #f7f7f6;
    --forest: #4f5f12;
    --forest-deep: #3d4b0c;
    --lime: #8db51a;
    --lime-bright: #a2c61f;
    --gold-light: #d8b07a;
    --gold: #b88a4e;
    --ink-soft: #4c5a14;
  }
  * { margin: 0; padding: 0; box-sizing: border-box; }
  html, body { width: 1200px; height: 934px; overflow: hidden; background: var(--bg); }
  body { font-family: "Montserrat", sans-serif; position: relative; }

  .label {
    position: absolute; left: 222px; top: 37px;
    width: 757px; height: 860px;
    background: var(--paper);
    box-shadow: 0 6px 24px rgba(0,0,0,0.08);
    overflow: hidden;
  }
  .label__top-band {
    position: absolute; left: 0; top: 0; width: 100%; height: 24px;
    background: linear-gradient(90deg, var(--forest-deep), var(--forest), var(--forest-deep));
  }
  .label__bottom-band {
    position: absolute; left: 0; bottom: 0; width: 100%; height: 20px;
    background: linear-gradient(90deg, var(--gold), var(--gold-light), var(--gold));
  }

  .badge-rail {
    position: absolute; left: 66px; top: 24px; width: 83px; height: 563px;
    background: var(--forest);
    border-radius: 0 0 42px 42px;
    display: flex; flex-direction: column; align-items: center;
    padding-top: 62px; gap: 22px;
  }
  .badge { display: flex; flex-direction: column; align-items: center; color: #eef0e0; }
  .badge svg { width: 46px; height: 46px; }
  .badge__text {
    font-family: "Oswald", sans-serif; font-weight: 300;
    font-size: 12px; line-height: 13px; text-align: center; margin-top: 6px;
    letter-spacing: 0.2px;
  }

  .count-tab {
    position: absolute; left: 66px; bottom: 20px; width: 83px; height: 190px;
    background: linear-gradient(180deg, var(--gold-light), var(--gold));
    border-radius: 42px 42px 0 0;
    color: #fff; text-align: center; padding-top: 50px;
  }
  .count-tab__number { font-size: 40px; font-weight: 300; line-height: 1; }
  .count-tab__unit { font-size: 13px; font-weight: 300; margin-top: 4px; letter-spacing: 0.5px; }
  .count-tab__type { font-size: 14px; font-weight: 800; line-height: 1; }
  .count-tab__sub { font-size: 8px; font-weight: 800; }

  .brand-block {
    position: absolute; left: 160px; right: 20px; top: 210px; text-align: center;
  }
  .brand-block__maker { color: var(--lime); font-size: 40px; font-weight: 600; }
  .brand-block__name {
    color: var(--forest); font-size: 50px; font-weight: 800; line-height: 1.15;
    margin-top: 12px; letter-spacing: 0.5px;
  }
  .brand-block__name-accent { color: var(--lime); display: block; }
  .brand-block__name sup { font-size: 22px; vertical-align: 24px; }

  .benefits { position: absolute; left: 160px; right: 20px; top: 525px; text-align: center; }
  .benefits__intro { color: var(--ink-soft); font-size: 29px; font-weight: 300; }
  .benefits__list {
    display: flex; justify-content: space-between; margin: 26px 22px 0 30px;
    color: var(--forest-deep); font-size: 20px; font-weight: 800;
  }

  .flavor-pill {
    position: absolute; left: 272px; top: 762px; width: 358px; height: 38px;
    background: linear-gradient(90deg, var(--lime), var(--lime-bright));
    border-radius: 19px; color: var(--forest-deep);
    font-size: 19px; font-weight: 500;
    display: flex; align-items: center; justify-content: center;
  }
</style>
</head>
<body>
  <main class="label">
    <div class="label__top-band"></div>

    <aside class="badge-rail">
      <div class="badge">
        <svg viewBox="0 0 46 46" fill="none" stroke="currentColor" stroke-width="1.5">
          <circle cx="23" cy="23" r="21"/>
          <path d="M14 32 L16 15 Q23 11 30 15 L32 32 Q23 35 14 32 Z"/>
          <path d="M19 18 L18 28"/>
        </svg>
        <span class="badge__text">GELATIN<br>FREE</span>
      </div>
      <div class="badge">
        <svg viewBox="0 0 46 46" fill="none" stroke="currentColor" stroke-width="1.5">
          <circle cx="23" cy="23" r="21"/>
          <path d="M12 25 H34 Q32 33 23 33 Q14 33 12 25 Z"/>
          <path d="M23 25 Q22 17 29 13 Q30 20 23 25"/>
          <path d="M21 25 Q17 19 13 19 Q15 24 21 25"/>
        </svg>
        <span class="badge__text">PLANT<br>BASED</span>
      </div>
      <div class="badge">
        <svg viewBox="0 0 46 46" fill="none" stroke="currentColor" stroke-width="1.5">
          <circle cx="23" cy="23" r="21"/>
          <path d="M23 34 V22"/>
          <path d="M23 24 Q24 15 32 13 Q32 22 23 24"/>
          <path d="M23 26 Q16 25 14 18 Q21 18 23 26"/>
        </svg>
        <span class="badge__text">VEGAN<br>FRIENDLY</span>
      </div>
      <div class="badge">
        <svg viewBox="0 0 46 46" fill="none" stroke="currentColor" stroke-width="1.5">
          <circle cx="23" cy="23" r="21"/>
          <path d="M15 33 Q31 23 31 13"/>
          <path d="M15 13 Q15 23 31 33"/>
          <path d="M18 17 H28 M17 22 H29 M18 28 H28"/>
          <path d="M9 37 L37 9"/>
        </svg>
        <span class="badge__text">NON<br>GMO</span>
      </div>
    </aside>

    <section class="brand-block">
      <p class="brand-block__maker">RT Dalloway's</p>
      <h1 class="brand-block__name">LEAFY BLENDBITE<span class="brand-block__name-accent">CHEWS<sup>™</sup></span></h1>
    </section>

    <section class="benefits">
      <p class="benefits__intro">SUPER GREENS BLEND FOR:</p>
      <p class="benefits__list"><span>ENERGY</span><span>DIGESTION</span><span>IMMUNE SUPPORT*</span></p>
    </section>

    <div class="count-tab">
      <p class="count-tab__number">60</p>
      <p class="count-tab__unit">GUMMIES</p>
      <p class="count-tab__type">DIETARY</p>
      <p class="count-tab__sub">SUPPLEMENT</p>
    </div>

    <p class="flavor-pill">Raspberry Flavor Gummies</p>

    <div class="label__bottom-band"></div>
  </main>
</body>
</html>
```